Website: Brightkeel Business Consultants, Qianhai SEZ, China

Our client is a business consultancy firm and will be the first to set up in the Qianhai Shenzhen-Hong Kong Modern Service Industry Cooperation Zone, China So we need a corporate website concept that engages service, finance and technology sector companies. The company can provide all the necessary services needed to set up shop in Qianhai. They are looking for a modern, international, reliable and strong image.

Here are some websites for reference prupose:

http://www.vornamesh.com/ (we like the dynamic banner and clear, clean layout of this website)

http://www.plendaradvisory.com/ (we like the background city image, use of light font, hover over menu functions and color scheme - purple and grey)

http://www.quolb.com/ (we like the simplicity of this website, clear lines and we like the dynamic banner)
Updates

Hello, We are currently undecided between three logo designs.  All three have been uploaded to the design brief so that you can use them as reference for the website design. Thx

Also please take note of the addition menu selection 'About Qianhai'. Thx

Hello all Designers, First of all we want thank you for participating in our website competition, the calibre of design was high and we appreciated the expedience. Our company is Lumenpath Web Design and Internet Marketing based in Shenzhen, China. We anticipate rapid growth in the Chinese domestic market as the country shifts in to a service sector economy. We hope to continue building reliable working relationships with you based on idea sharing and constructive feedback. Once again, Thankyou, LP Team

Target Market(s)

International finance and technology companies looking to set up in Qianhai Special Economic Zone, China

Industry/Entity Type

Finance

Requirements
Must have
• Initial design for home page and in later selection stages a secondary page will be required.

The design should be for PSD concepts only no code!

Menu bar, Photo banner -
A. Photo banner and text overlay,
B.Photo Banner and text description to left or right.

Social Connect icons, Site search bar (top right), Logo space (top left).

Menu bar at top with Home, About Us, About Qianhai, Services, Portfolio, Partners, Our Team Contact Us.

Standard 3-4 box layout - Banner at top and 2-3 boxes under banner.

Colour scheme- A. Purple and Blue, must have light background/body
B. Shades of white, black and grey.

Simple, clear, clean, sharp.

```html
<!DOCTYPE html>
<html lang="en">
<head>
<meta charset="utf-8">
<title>Brightkeel Business Consulting</title>
<link href="https://fonts.googleapis.com/css2?family=Arimo:wght@400;700&family=Poiret+One&display=swap" rel="stylesheet">
<style>
  :root {
    --ink: #333333;
    --rule: #cfcfcf;
    --nav-bg: #f7f7f8;
    --link-blue: #2f8fd8;
    --purple: #4b1d55;
    --purple-deep: #3a0f3f;
    --plum-text: #6a2b74;
    --logo-pink: #b0358f;
    --teal: #2f6f8e;
    --card-blue: #1b5f97;
    --button-blue: #cfe6f7;
    --arrow-blue: #1b5f97;
    --city-dark: #2b3a4a;
    --city-light: #8fa8bc;
  }
  * { box-sizing: border-box; margin: 0; padding: 0; }
  html, body { width: 1120px; height: 1200px; overflow: hidden; background: #ffffff; }
  body { font-family: "Arimo", Arial, sans-serif; color: var(--ink); }
  .page { position: relative; width: 1100px; height: 1200px; margin: 0 10px; }

  .topbar { position: absolute; left: -10px; top: 0; width: 1120px; height: 37px; border-bottom: 1px solid var(--rule); }
  .social { position: absolute; right: 125px; top: 11px; display: flex; gap: 12px; list-style: none; }
  .social li { display: flex; align-items: center; gap: 4px; font-size: 10px; color: #555; }
  .social li::before { content: ""; width: 9px; height: 9px; background: var(--card-blue); }

  .brand { position: absolute; left: 100px; top: 110px; }
  .brand-name { font-size: 22px; letter-spacing: 1px; color: var(--logo-pink); display: flex; align-items: center; gap: 8px; }
  .brand-name::before { content: ""; width: 18px; height: 18px; border-radius: 50%; background: var(--card-blue); }
  .brand-tag { font-size: 9px; letter-spacing: 4.5px; color: #555; margin-top: 4px; padding-left: 26px; }

  .search { position: absolute; left: 832px; top: 66px; width: 174px; height: 23px; border: 1px solid #d8c4d8; background: #fdf4fb; display: flex; }
  .search span { flex: 1; font-size: 13px; color: #999; padding: 3px 0 0 24px; border-right: 1px solid #ccc; }
  .search svg { margin: 4px 12px 0 14px; }

  .nav { position: absolute; left: 345px; top: 116px; width: 662px; height: 55px; background: var(--nav-bg); border: 1px solid #dedede; display: flex; align-items: center; padding-left: 10px; list-style: none; font-size: 13px; }
  .nav li { color: #333; }
  .nav li.active { color: var(--link-blue); }
  .nav li + li::before { content: "/"; color: #aaa; margin: 0 11px 0 12px; }

  .banner { position: absolute; left: 90px; top: 204px; width: 921px; height: 394px; border: 1px solid #d6d6d6; padding: 3px; }
  .banner-photo { width: 913px; height: 386px; background: linear-gradient(180deg, #a7bccc 0%, #6f8aa0 35%, var(--city-dark) 100%); position: relative; }
  .banner-panel { position: absolute; left: 0; top: 0; width: 294px; height: 386px; background: linear-gradient(180deg, rgba(88,50,110,.92), rgba(60,20,70,.95)); padding: 88px 24px 0 32px; color: #fff; }
  .arrows { position: absolute; left: 30px; top: 30px; display: flex; gap: 10px; }
  .banner-panel h1 { font-size: 24px; line-height: 24px; font-weight: 700; }
  .banner-panel .lead { margin-top: 24px; font-size: 14px; line-height: 16px; color: #d9cfe0; letter-spacing: .3px; }
  .banner-panel .note { position: absolute; left: 32px; top: 297px; width: 250px; font-size: 10.5px; line-height: 13px; color: #c9bdd2; }

  .tagline { position: absolute; left: 0; top: 604px; width: 1100px; text-align: center; }
  .tagline h2 { font-family: "Poiret One", sans-serif; font-size: 30px; font-weight: 400; color: var(--teal); letter-spacing: 1px; }
  .tagline p { font-size: 15px; color: var(--purple); margin-top: 4px; letter-spacing: .5px; }

  .rule { position: absolute; left: -10px; width: 1120px; border-top: 1px solid var(--rule); }

  .section-title { position: absolute; font-family: "Poiret One", sans-serif; font-size: 20px; color: var(--plum-text); display: flex; align-items: center; gap: 8px; }
  .section-title::before { content: ""; border-left: 6px solid var(--arrow-blue); border-top: 5px solid transparent; border-bottom: 5px solid transparent; }

  .card { position: absolute; top: 730px; width: 218px; height: 237px; border: 1px solid #ddd; }
  .card-photo { position: absolute; left: 3px; top: 3px; width: 210px; height: 174px; }
  .card-body { position: absolute; left: -1px; top: 179px; width: 218px; height: 57px; background: var(--card-blue); padding: 3px 0 0 28px; color: #fff; font-size: 11.5px; line-height: 12px; }
  .card-body .more { display: inline-block; margin-top: 8px; background: var(--button-blue); color: #1a2d40; border: 1px solid #fff; font-size: 11px; padding: 1px 6px; }

  .clients-line { position: absolute; top: 1025px; height: 56px; border-left: 1px solid #bbb; }
  .client { position: absolute; top: 1025px; width: 106px; height: 57px; border: 1px solid #cfcfcf; display: flex; align-items: center; justify-content: center; font-size: 14px; font-weight: 700; color: #333; box-shadow: 0 1px 2px rgba(0,0,0,.12); }

  .footer { position: absolute; left: -10px; top: 1108px; width: 1120px; height: 92px; background: radial-gradient(ellipse at 50% 40%, #6a2f6d 0%, var(--purple-deep) 80%); color: #fff; }
  .footer-nav { display: flex; justify-content: center; list-style: none; font-size: 12px; padding-top: 16px; margin-left: -12px; }
  .footer-nav li + li::before { content: "|"; color: #a98aab; margin: 0 20px; }
  .copyright { text-align: center; font-size: 11.5px; margin-top: 19px; margin-left: -10px; letter-spacing: .3px; }
</style>
</head>
<body>
<div class="page">
  <header class="topbar">
    <ul class="social">
      <li>Friendly</li><li>Chirper</li><li>Plusring</li><li>Photodot</li><li>Pinboardly</li>
    </ul>
  </header>

  <div class="brand">
    <div class="brand-name">BRIGHTKEEL</div>
    <div class="brand-tag">BUSINESS CONSULTING</div>
  </div>

  <div class="search">
    <span>search</span>
    <svg width="14" height="14" viewBox="0 0 14 14"><circle cx="5" cy="5" r="3.6" fill="none" stroke="#999" stroke-width="1.6"/><line x1="7.6" y1="7.6" x2="12.5" y2="12.5" stroke="#999" stroke-width="2"/></svg>
  </div>

  <ul class="nav">
    <li class="active">Home</li><li>About Us</li><li>About Qianhai</li><li>Services</li><li>Portfolio</li><li>Partners</li><li>Our Team</li><li>contact Us</li>
  </ul>

  <section class="banner">
    <div class="banner-photo" role="img" aria-label="Night skyline of a harbour city with towers and water">
      <div class="banner-panel">
        <div class="arrows">
          <svg width="10" height="14" viewBox="0 0 10 14"><polyline points="8,1 2,7 8,13" fill="none" stroke="#fff" stroke-width="2.4"/></svg>
          <svg width="10" height="14" viewBox="0 0 10 14"><polyline points="2,1 8,7 2,13" fill="none" stroke="#fff" stroke-width="2.4"/></svg>
        </div>
        <h1>Nemo enim ipsam voluptatem quia voluptas sit</h1>
        <p class="lead">sed quia consequuntur magni eos qui ratione voluptatem sequi nesciunt.</p>
        <p class="note">eaque ipsa quae ab illo inventore veritatis et quasi architecto beatae vitae dicta sunt explicabo.</p>
      </div>
    </div>
  </section>

  <div class="tagline">
    <h2>Sed ut perspiciatis unde omnis iste natus error sit</h2>
    <p>laudantium, totam rem aperiam</p>
  </div>

  <div class="rule" style="top:684px"></div>

  <h3 class="section-title" style="left:96px; top:694px;">Lorem Ipsum</h3>

  <article class="card" style="left:92px">
    <div class="card-photo" role="img" aria-label="Close-up of a hand adjusting a wristwatch on a shirt cuff" style="background:linear-gradient(135deg,#f3ebe6,#cdb9ad)"></div>
    <div class="card-body">Lorem ipsum dolor sit amet,<br>consectetur adipisicing elit...<br><span class="more">Read More</span></div>
  </article>
  <article class="card" style="left:325px">
    <div class="card-photo" role="img" aria-label="Business team standing in a bright office" style="background:linear-gradient(135deg,#c9d6e2,#3a4a5e)"></div>
    <div class="card-body">Lorem ipsum dolor sit amet,<br>consectetur adipisicing elit...<br><span class="more">Read More</span></div>
  </article>
  <article class="card" style="left:558px">
    <div class="card-photo" role="img" aria-label="Businessman in a suit in front of city towers" style="background:linear-gradient(180deg,#d8e2ec,#6d7885)"></div>
    <div class="card-body">Lorem ipsum dolor sit amet,<br>consectetur adipisicing elit...<br><span class="more">Read More</span></div>
  </article>
  <article class="card" style="left:792px">
    <div class="card-photo" role="img" aria-label="Hands typing on a laptop keyboard" style="background:linear-gradient(135deg,#f2f2f2,#4a4a4a)"></div>
    <div class="card-body">Lorem ipsum dolor sit amet,<br>consectetur adipisicing elit...<br><span class="more">Read More</span></div>
  </article>

  <div class="rule" style="top:998px"></div>

  <h3 class="section-title" style="left:96px; top:1042px;">Our Clients</h3>
  <div class="clients-line" style="left:301px"></div>
  <div class="client" style="left:332px">Norvane</div>
  <div class="client" style="left:468px">Fizzwell</div>
  <div class="client" style="left:604px">Kestrel</div>
  <div class="client" style="left:740px">Datamere</div>
  <div class="clients-line" style="left:877px"></div>

  <footer class="footer">
    <ul class="footer-nav">
      <li>Home</li><li>About Us</li><li>About Qianhai</li><li>Services</li><li>Portfolio</li><li>Partners</li><li>Our Team</li><li>Contact Us</li>
    </ul>
    <p class="copyright">copyright © 2013 Brightkeel. All Rights Reserved</p>
  </footer>
</div>
</body>
</html>
```